Brisel Home Care Brochure for Recruiting Clients

I need a brochure made for a home care company called 'Brisel Home Care'. I have uploaded the logo, location, and a few items about our company and what it offers. The final design should communicate trust and respect for patients and their families. I will probably be changing the phone number in the next few days so will need to add a new number and more serving locations.

Industry/Entity Type

Home Health Care

Colors
0555a3
ffffff
3176b5
85acd3
0392cd

Requirements
Must have
• Hello All,
• Thank you kindly for your patience. Please add the changes below to the brochures:
• Phone number: 571-555-0143
• Email: briselhc@quorvamail.com
• Homepage: [Non image link removed]Service Locations: Arlington County, Fairfax County, Fauquier County, Loudoun County, Prince William County
• Also please note the additional sentence at the end of the following key points:
• ABOUT US:
• Brisel serves to give patients the personal care they need in order for them to continue to live dignified and independent lives in the comfort of their homes. We begin by assessing and understanding our patient’s individual needs and met those needs through selectively assigning qualified, trustworthy and compassionate home care aids. Brisel holds great pride in keeping our client’s health, quality of life and well-being central in the design and delivery of our services. Our services can prevent re-hospitalization, postpone institutionalization, and reduce the need for urgent care.
• ABOUT OUR SERVICE PROVIDERS:
• We go through a rigorous in-depth application process with all of our service providers, so that you can rest assure that your home care provider is most qualified to meet your needs. Our application process also includes a thorough screening, criminal background check, DMV driving history and a comprehensive exam. Our service providers are trained, monitored, and tested continuously to meet our high standards of work ethic and professionalism. Our care providers are covered by professional liability, bonding, and workers’ compensation insurance. At Brisel teamwork among members is of key importance and it is how we conduct our day to day business. We work as a team with family, patient and their provider in developing an ideal care plan for the patient.
• OUR SERVICES:
• Companionship Services Include:
• - Offer companionship and conversation - Supervise home maintenance
• - Mail bills and letters
• - Provide reminders for appointments
• - Arrange appointments
• - Maintain calendar
• - Plan visits, outings and trips
• - Visit friends
• - Prepare grocery list
• - Assist with clothing selection
• - Stimulate mental awareness
• - Aid with reading
• - Monitor diet and eating
• - Check food expirations
• - Assist with morning and wake-up
• - Assist with evening and tuck-in
• - Provide respite care
• - Provide medication reminders
• - Assist with walking
• - Write letters and correspondence
• - Organize mail
• - Care for house plants
• - Answer the door
• - Assist with entertaining
• - Play games and cards
• - Rent and play movies
• - Oversee home deliveries
• - Supervise home maintenance
• - Discuss current and historical events - Reminisce about the past
• Home Helper Services Include:
• - Assist with laundry and ironing
• - Organize and clean closets
• - Assist with pet care
• - Attend social and sporting events - Accompany to lunch or dinner
• - Care for Alzhiemers
• - Change linens
• - Dust furniture
• - Drop off and pick up dry cleaning
• - Escort for shopping and errands
• - Escort to appointments
• - Escort to religious services
• - Help with airport task
• - Pick up prescriptions
• - Make beds
• - Prepare meals
• - Plan, prepare, and clean-up meals - Prepare future meals
• - Provide light housekeeping
• - Take out garbage
• Personal Services Include:
• - Ambulation
• - Bathing
• - Cognitive impairment - Mobility
• - Transferring
• - Incontinence
• - Dressing
• - Eating
• - Grooming
Nice to have
• Nice pictures of elderly clients with helpers or nurse.

```html
<!DOCTYPE html>
<html lang="en">
<head>
<meta charset="utf-8">
<title>Brisel Home Care – Tri-fold Brochure</title>
<link href="https://fonts.googleapis.com/css2?family=Arimo:wght@400;700&display=swap" rel="stylesheet">
<style>
  :root {
    --navy: #0555a3;
    --navy-deep: #123576;
    --navy-dark: #0d2a63;
    --mid-blue: #3176b5;
    --soft-blue: #85acd3;
    --cyan: #0392cd;
    --cream: #f8f5f1;
    --white: #ffffff;
    --ink: #2c3340;
    --stage: #d9d9d9;
  }
  * { box-sizing: border-box; margin: 0; padding: 0; }
  html, body {
    width: 1200px; height: 855px; overflow: hidden;
    background: var(--stage);
    font-family: "Arimo", Arial, sans-serif;
  }
  .brochure {
    position: absolute; left: 60px; top: 47px;
    width: 1080px; height: 760px;
    box-shadow: 0 10px 30px rgba(0,0,0,.18);
  }
  .brochure-art { position: absolute; inset: 0; display: block; }
  .panel { position: absolute; top: 0; width: 360px; height: 760px; }
  .panel--about { left: 0; }
  .panel--contact { left: 360px; color: var(--white); text-align: center; }
  .panel--cover { left: 720px; }

  .about-title {
    position: absolute; left: 34px; top: 52px;
    font-size: 19px; font-weight: 400; color: var(--navy); letter-spacing: .5px;
  }
  .about-text {
    position: absolute; left: 34px; top: 88px; width: 300px;
    font-size: 13.5px; line-height: 1.3; color: var(--ink); text-align: justify;
  }
  .about-text p + p { margin-top: 16px; }

  .contact-title {
    position: absolute; left: 0; right: 0; top: 58px;
    font-size: 20px; font-weight: 700; letter-spacing: .5px;
  }
  .contact-address {
    position: absolute; left: 0; right: 0; top: 96px;
    font-size: 15px; line-height: 1.3; font-style: normal;
  }
  .contact-locations {
    position: absolute; left: 28px; right: 28px; top: 152px;
    font-size: 12.5px; line-height: 1.35;
  }
  .contact-call {
    position: absolute; left: 0; right: 0; top: 566px;
    font-size: 15px; font-weight: 700; line-height: 1.35;
  }
  .contact-web {
    position: absolute; left: 0; right: 0; top: 676px;
    font-size: 15px; font-weight: 700; color: var(--navy); letter-spacing: .6px;
  }

  .brand {
    position: absolute; left: 0; right: 0; top: 628px;
    display: flex; align-items: center; justify-content: center; gap: 12px;
  }
  .brand-mark {
    width: 30px; height: 30px; border-radius: 50%;
    background: var(--cyan);
  }
  .brand-name {
    font-size: 26px; font-weight: 400; color: var(--white);
  }
</style>
</head>
<body>
  <main class="brochure">
    <svg class="brochure-art" width="1080" height="760" viewBox="0 0 1080 760" aria-hidden="false">
      <defs>
        <linearGradient id="contactGradient" x1="0" y1="0" x2="0" y2="1">
          <stop offset="0" stop-color="#0f3d86"/>
          <stop offset="1" stop-color="#173a7a"/>
        </linearGradient>
        <linearGradient id="waveGradient" x1="0" y1="0" x2="1" y2="1">
          <stop offset="0" stop-color="#1f82c4"/>
          <stop offset="1" stop-color="#0a6aae"/>
        </linearGradient>
        <linearGradient id="photoWarm" x1="0" y1="0" x2="1" y2="1">
          <stop offset="0" stop-color="#c9b8a8"/>
          <stop offset=".5" stop-color="#e8dcd2"/>
          <stop offset="1" stop-color="#b8c7dc"/>
        </linearGradient>
        <linearGradient id="photoCool" x1="0" y1="0" x2="1" y2="1">
          <stop offset="0" stop-color="#e3ecf4"/>
          <stop offset=".5" stop-color="#9cc6de"/>
          <stop offset="1" stop-color="#e6e0d6"/>
        </linearGradient>
      </defs>

      <!-- About panel -->
      <rect class="about-bg" x="0" y="0" width="360" height="760" fill="var(--cream)"/>
      <path class="about-band" d="M0,438 Q180,398 360,340 L360,372 Q180,432 0,472 Z" fill="var(--cyan)"/>
      <g role="img" aria-label="Photo of a smiling caregiver embracing an elderly man at home">
        <path d="M0,480 Q180,440 360,382 L360,760 L0,760 Z" fill="url(#photoWarm)"/>
      </g>

      <!-- Contact panel -->
      <rect class="contact-bg" x="360" y="0" width="360" height="760" fill="url(#contactGradient)"/>
      <path class="contact-wave" d="M360,418 Q540,450 720,400 L720,760 L360,760 Z" fill="url(#waveGradient)"/>
      <path class="contact-footer" d="M360,662 Q540,636 720,580 L720,760 L360,760 Z" fill="var(--cream)"/>
      <g role="img" aria-label="Street map showing the office location">
        <circle cx="540" cy="380" r="108" fill="#d3d6da" stroke="var(--white)" stroke-width="4"/>
      </g>

      <!-- Cover panel -->
      <rect class="cover-bg" x="720" y="0" width="360" height="760" fill="var(--navy-deep)"/>
      <path class="cover-cream" d="M720,470 Q900,540 1080,440 L1080,490 Q900,590 720,520 Z" fill="var(--cream)"/>
      <path class="cover-band" d="M720,448 Q900,520 1080,418 L1080,446 Q900,548 720,476 Z" fill="var(--cyan)"/>
      <g role="img" aria-label="Photo of a nurse in blue scrubs with a smiling elderly woman holding papers">
        <path d="M720,0 L1080,0 L1080,420 Q900,522 720,450 Z" fill="url(#photoCool)"/>
      </g>

      <!-- Fold lines -->
      <line x1="360" y1="0" x2="360" y2="760" stroke="rgba(0,0,0,.06)"/>
      <line x1="720" y1="0" x2="720" y2="760" stroke="rgba(0,0,0,.06)"/>
    </svg>

    <section class="panel panel--about">
      <h2 class="about-title">ABOUT US</h2>
      <div class="about-text">
        <p>Brisel serves to give patients the personal care they need in order for them to continue to live dignified and independent lives in the comfort of their homes.</p>
        <p>We begin by assessing and understanding our patient’s individual needs and met those needs through selectively assigning qualified, trustworthy and compassionate home care aids.</p>
        <p>Brisel holds great pride in keeping our client’s health, quality of life and well-being central in the design and delivery of our services.</p>
      </div>
    </section>

    <section class="panel panel--contact">
      <h2 class="contact-title">CONTACT US</h2>
      <address class="contact-address">417 Marrow Street,<br>Falls Church, VA 22046</address>
      <p class="contact-locations">Service Locations: Arlington County, Fairfax County, Fauquier County, Loudoun County, Prince William County</p>
      <p class="contact-call">Call us now at 571-555-0143<br>briselhc@quorvamail.com</p>
      <p class="contact-web">www.briselhomecare.org</p>
    </section>

    <section class="panel panel--cover">
      <div class="brand">
        <span class="brand-mark"></span>
        <span class="brand-name">Brisel Home Care</span>
      </div>
    </section>
  </main>
</body>
</html>
```